HUSH: Halt Usual Stuff Happily school library event

I need two poster designs for Halt Usual Stuff Happily (HUSH) in BC, requested by the CSMKA--Cedarvale School Media Keepers' Association. One should be for elementary students and one for high school. I want the date (Monday, October 26, 2020) and Halt Usual Stuff Happily. I would like the posters in English and in French. French is : Mets Ta Journée En Pause! I'm including last year's posters as examples. I would like to be able to print the poster files on 11x17 paper.

Requirements
Must have
• -The phrase "Halt Usual Stuff Happily" for the English version; "Mets Ta Journée En Pause" for the French version.
-Include the organization name: Cedarvale School Media Keepers' Association
-The date: Monday, October 26, 2020
Nice to have
• I would like the elementary version to be bright and colourful--fun for younger kids. I would like the high school version to be a bit more mature for the older students. Can still be bright and colourful.

```html
<!DOCTYPE html>
<html lang="en">
<head>
<meta charset="utf-8">
<title>HUSH posters – Cedarvale School Media Keepers' Association</title>
<link rel="stylesheet" href="https://fonts.googleapis.com/css2?family=Montserrat:wght@600;700&family=Dancing+Script:wght@600&display=swap">
<style>
  :root {
    --sheet: #e6e6e6;
    --teal: #5a9fac;
    --cyan: #7fd0dc;
    --yellow: #f1b80f;
    --cream: #f5efcb;
    --red: #cc5a49;
    --navy: #1a3550;
    --white: #ffffff;
    --lime: #a9c93a;
    --mint: #3fbf8a;
    --gold: #efb400;
    --blue: #2747b8;
  }
  * { box-sizing: border-box; margin: 0; padding: 0; }
  html, body { width: 881px; height: 1200px; overflow: hidden; }
  body {
    background: linear-gradient(180deg, #dedede 0%, #f4f4f4 100%);
    position: relative;
    font-family: "Montserrat", sans-serif;
    color: var(--white);
  }
  .poster {
    position: absolute;
    width: 356px;
    height: 552px;
    overflow: hidden;
  }
  .poster--row1 { top: 38px; }
  .poster--row2 { top: 606px; }
  .poster--col1 { left: 70px; }
  .poster--col2 { left: 448px; }
  .poster__bg, .poster__frame { position: absolute; inset: 0; }
  .poster__frame { z-index: 5; pointer-events: none; }
  .presenter {
    position: absolute; top: 17px; left: 0; width: 100%;
    text-align: center; font-size: 11.5px; font-weight: 600;
    line-height: 1.4; text-transform: uppercase; z-index: 6;
  }
  .title {
    position: absolute; left: 0; width: 100%; text-align: center;
    font-weight: 600; text-transform: uppercase; z-index: 6;
    white-space: nowrap;
  }
  .connector {
    position: absolute; left: 0; width: 100%; text-align: center;
    font-family: "Dancing Script", cursive; font-size: 24px; z-index: 6;
  }
  .date {
    position: absolute; bottom: 13px; font-size: 15px; font-weight: 600;
    z-index: 6; white-space: nowrap; line-height: 1;
  }

  /* Elementary */
  .poster--kids .title { top: 82px; font-size: 26px; }
  .poster--kids .connector { top: 110px; }
  .book {
    position: absolute; top: 132px; left: 8px; width: 340px; height: 150px;
    background: linear-gradient(180deg, var(--cream) 0%, #ece2b0 100%);
    clip-path: polygon(4% 10%, 50% 4%, 96% 10%, 100% 100%, 50% 92%, 0 100%);
    z-index: 2;
  }
  .book__word {
    position: absolute; top: 148px; left: 0; width: 100%; text-align: center;
    font-weight: 700; font-size: 54px; letter-spacing: 4px; z-index: 3;
  }
  .book__word .c1 { color: var(--lime); }
  .book__word .c2 { color: var(--mint); }
  .book__word .c3 { color: var(--gold); }
  .book__word .c4 { color: var(--blue); }
  .photo-main {
    position: absolute; top: 270px; left: 8px; width: 340px; height: 250px;
    background: linear-gradient(135deg, #c9d3da 0%, #e7e3dd 55%, #b49a7e 100%);
    z-index: 1;
  }
  .photo-circle {
    position: absolute; left: 22px; width: 130px; height: 130px; border-radius: 50%;
    z-index: 2;
  }
  .photo-circle--top { top: 288px; border: 2px solid var(--yellow); background: linear-gradient(135deg, #eae6e2, #9c3a40); }
  .photo-circle--bottom { top: 408px; border: 2px solid var(--cyan); background: linear-gradient(135deg, #e4c9a2, #d9602f); }
  .poster--kids .date { right: 20px; }

  /* High school */
  .photo-field {
    position: absolute; top: 46px; left: 8px; width: 340px; height: 222px;
    background: linear-gradient(180deg, #b6b7ad 0%, #8b7f63 40%, #7e8f57 70%, #93a36a 100%);
    z-index: 1;
  }
  .poster--teen .title { top: 284px; font-size: 26px; }
  .poster--teen .connector { top: 312px; }
  .big-word {
    position: absolute; left: 0; width: 100%; text-align: center;
    font-weight: 700; color: var(--navy); z-index: 3; line-height: 1;
  }
  .poster--teen .date { left: 0; width: 100%; text-align: center; }
</style>
</head>
<body>

<!-- English, elementary -->
<section class="poster poster--kids poster--row1 poster--col1">
  <svg class="poster__bg" viewBox="0 0 356 552">
    <rect width="356" height="552" fill="var(--teal)"/>
  </svg>
  <h2 class="title">Halt Usual Stuff</h2>
  <p class="connector">and</p>
  <div class="book" role="img" aria-label="Illustration of an open book"></div>
  <p class="book__word"><span class="c1">H</span><span class="c2">A</span><span class="c3">P</span><span class="c4">P</span><span class="c1">I</span><span class="c2">L</span><span class="c3">Y</span></p>
  <div class="photo-main" role="img" aria-label="Photo of a girl reading a book on the floor"></div>
  <div class="photo-circle photo-circle--top" role="img" aria-label="Photo of a child reading with a toy"></div>
  <div class="photo-circle photo-circle--bottom" role="img" aria-label="Photo of two boys reading a book"></div>
  <svg class="poster__frame" viewBox="0 0 356 552">
    <path d="M0 0H356V52Q178 72 0 52Z" fill="var(--cyan)"/>
    <path d="M0 516Q178 494 356 516V552H0Z" fill="var(--yellow)"/>
    <rect x="8" y="8" width="340" height="536" fill="none" stroke="var(--white)" stroke-width="2"/>
  </svg>
  <p class="presenter">Cedarvale School Media Keepers'<br>Association presents:</p>
  <p class="date">Monday, October 26, 2020</p>
</section>

<!-- English, high school -->
<section class="poster poster--teen poster--row1 poster--col2">
  <svg class="poster__bg" viewBox="0 0 356 552">
    <rect width="356" height="552" fill="var(--white)"/>
    <path d="M0 266H356V330Q260 330 178 360Q96 330 0 330Z" fill="var(--red)"/>
  </svg>
  <div class="photo-field" role="img" aria-label="Photo of two teens reading back to back on a blanket in a field"></div>
  <h2 class="title">Halt Usual Stuff</h2>
  <p class="connector">and</p>
  <p class="big-word" style="top:380px;font-size:62px;">HAPPILY</p>
  <svg class="poster__frame" viewBox="0 0 356 552">
    <path d="M0 0H356V52Q178 66 0 52Z" fill="var(--teal)"/>
    <path d="M0 516Q178 498 356 516V552H0Z" fill="var(--teal)"/>
    <rect x="1.5" y="1.5" width="353" height="549" fill="none" stroke="var(--teal)" stroke-width="3"/>
    <rect x="8" y="8" width="340" height="536" fill="none" stroke="var(--white)" stroke-width="2"/>
  </svg>
  <p class="presenter">Cedarvale School Media Keepers'<br>Association presents:</p>
  <p class="date">Monday, October 26, 2020</p>
</section>

<!-- French, elementary -->
<section class="poster poster--kids poster--row2 poster--col1" lang="fr">
  <svg class="poster__bg" viewBox="0 0 356 552">
    <rect width="356" height="552" fill="var(--teal)"/>
  </svg>
  <h2 class="title">Mets Ta Journée</h2>
  <p class="connector">en</p>
  <div class="book" role="img" aria-label="Illustration d'un livre ouvert"></div>
  <p class="book__word" style="top:140px;font-size:64px;"><span class="c2">P</span><span class="c3">A</span><span class="c4">U</span><span class="c1">S</span><span class="c2">E</span></p>
  <div class="photo-main" role="img" aria-label="Photo d'une fille qui lit un livre"></div>
  <div class="photo-circle photo-circle--top" role="img" aria-label="Photo d'un enfant qui lit avec un jouet"></div>
  <div class="photo-circle photo-circle--bottom" role="img" aria-label="Photo de deux garçons qui lisent"></div>
  <svg class="poster__frame" viewBox="0 0 356 552">
    <path d="M0 0H356V52Q178 72 0 52Z" fill="var(--cyan)"/>
    <path d="M0 516Q178 494 356 516V552H0Z" fill="var(--yellow)"/>
    <rect x="8" y="8" width="340" height="536" fill="none" stroke="var(--white)" stroke-width="2"/>
  </svg>
  <p class="presenter" lang="en">Cedarvale School Media Keepers'<br>Association presents:</p>
  <p class="date">Lundi 26 octobre 2020</p>
</section>

<!-- French, high school -->
<section class="poster poster--teen poster--row2 poster--col2" lang="fr">
  <svg class="poster__bg" viewBox="0 0 356 552">
    <rect width="356" height="552" fill="var(--white)"/>
    <path d="M0 260H356V318Q260 318 178 350Q96 318 0 318Z" fill="var(--red)"/>
  </svg>
  <div class="photo-field" style="height:214px;" role="img" aria-label="Photo de deux ados qui lisent dos à dos dans un champ"></div>
  <h2 class="title" style="top:274px;">Mets Ta Journée</h2>
  <p class="connector" style="top:302px;">en</p>
  <p class="big-word" style="top:372px;font-size:88px;">PAUSE</p>
  <svg class="poster__frame" viewBox="0 0 356 552">
    <path d="M0 0H356V52Q178 66 0 52Z" fill="var(--teal)"/>
    <path d="M0 516Q178 498 356 516V552H0Z" fill="var(--teal)"/>
    <rect x="1.5" y="1.5" width="353" height="549" fill="none" stroke="var(--teal)" stroke-width="3"/>
    <rect x="8" y="8" width="340" height="536" fill="none" stroke="var(--white)" stroke-width="2"/>
  </svg>
  <p class="presenter" lang="en">Cedarvale School Media Keepers'<br>Association presents:</p>
  <p class="date">Lundi 26 octobre 2020</p>
</section>

</body>
</html>
```